Flyer Design Project

We would like a double sided a5 flyer. To promote our new brand which is velvetine mobile, attached is the logo. This is for a mobile telecom company.
The aim of the flyer is to create brand awareness, to pormote a managed service for mobile phone connections/ tariffs. For business users and also personal use.

We would like to focus to be on offshore billing and discrete billing for users based abroad. eg students

Theme should be based around Plumleaf and Zorphones , one side should focus on business users and the other should focus on personal use. The focus on business users should be based around , Virtual landline numbers, where users can have a landline number connected to their mobile phones.
Should be elegant, up class ,and not to much text bullet points would be good .

Branding of telecoms QX ,K7 ,Telmarix,.
Updates

Velvetine mobile

Contact info for the flyer. 
info@velvetinemobile.example
www.velvetinemobile.example
0871 463 19 19 

Flyers need to look elegant and good creative designs please.

Industry/Entity Type

Telecom

```html
<!DOCTYPE html>
<html lang="en">
<head>
<meta charset="utf-8">
<title>Velvetine mobile – flyer</title>
<link rel="stylesheet" href="https://fonts.googleapis.com/css2?family=Questrial&family=Nunito:wght@800;900&display=swap">
<style>
  :root {
    --page: #ffffff;
    --ink: #111111;
    --white: #ffffff;
    --band: #070707;
    --panel: rgba(128, 232, 58, 0.82);
    --photo-a: #c9c2e6;
    --photo-b: #8f8fd6;
    --photo-c: #5a6fc4;
    --photo-d: #e6e2f2;
    --device-a: #2a2a2e;
    --device-b: #6c7a96;
    --carrier: #1d3fa3;
  }
  * { margin: 0; padding: 0; box-sizing: border-box; }
  html, body { width: 1200px; height: 826px; overflow: hidden; background: var(--page); }
  body { position: relative; font-family: "Questrial", sans-serif; color: var(--ink); }

  .flyer { position: absolute; top: 36px; height: 757px; overflow: hidden; }
  .flyer--business { left: 37px; width: 567px; }
  .flyer--personal { left: 620px; width: 538px; }

  .backdrop {
    position: absolute; left: 0; top: 0; width: 100%;
    background:
      radial-gradient(ellipse 40% 30% at 45% 8%, rgba(240,170,150,0.75), transparent 70%),
      radial-gradient(ellipse 60% 50% at 30% 60%, var(--photo-d), transparent 70%),
      linear-gradient(160deg, var(--photo-a) 0%, var(--photo-b) 45%, var(--photo-c) 75%, var(--photo-a) 100%);
  }
  .flyer--business .backdrop { height: 591px; }
  .flyer--personal .backdrop { height: 631px; }

  .band { position: absolute; left: 0; bottom: 0; width: 100%; background: var(--band); color: var(--white); }
  .flyer--business .band { height: 166px; }
  .flyer--personal .band { height: 126px; }

  .panel {
    position: absolute; background: var(--panel); color: var(--white);
    font-size: 27px; line-height: 34px; padding: 6px 12px; border-radius: 2px;
  }

  .outlined {
    font-family: "Nunito", sans-serif; font-weight: 900; color: var(--white);
    -webkit-text-stroke: 1.6px var(--ink); paint-order: stroke fill;
  }

  /* business side */
  .lead { position: absolute; left: 18px; top: 24px; font-size: 33px; }
  .headline { position: absolute; left: 50px; top: 50px; font-size: 72px; line-height: 1.2; -webkit-text-stroke: 2.4px var(--ink); letter-spacing: -0.5px; }
  .tail { position: absolute; right: 52px; top: 132px; font-size: 33px; }
  .flyer--business .panel { left: 35px; width: 474px; }
  .contact-web { position: absolute; left: 0; width: 100%; top: 532px; text-align: center; font-size: 21px; }
  .contact-line { position: absolute; left: 31px; top: 563px; font-size: 16px; word-spacing: 1px; }
  .contact-line .tel { margin-left: 18px; }
  .brand-block { position: absolute; left: 0; width: 100%; top: 54px; text-align: center; }
  .brand-mark { display: inline-block; width: 14px; height: 14px; background: var(--white); margin-bottom: 18px; }
  .brand-name { display: block; font-size: 21px; letter-spacing: 1px; }

  /* personal side */
  .question { position: absolute; left: 0; width: 100%; top: 22px; text-align: center; font-size: 39px; line-height: 54px; letter-spacing: 0.5px; }
  .flyer--personal .panel { left: 33px; width: 474px; height: 83px; padding-top: 8px; font-size: 27px; }
  .devices { position: absolute; left: 35px; top: 492px; width: 127px; height: 124px; border-radius: 10px;
    background: linear-gradient(120deg, var(--device-a) 0%, var(--device-b) 50%, var(--device-a) 100%); }
  .invite { position: absolute; left: 170px; top: 494px; font-size: 26px; line-height: 36px; -webkit-text-stroke: 1.3px var(--ink); }
  .carriers { position: absolute; left: 392px; top: 585px; display: flex; gap: 8px; align-items: center; font-size: 15px; color: var(--carrier); }
  .carriers .dot { width: 8px; height: 8px; border-radius: 50%; background: var(--carrier); }
  .flyer--personal .band .web { position: absolute; left: 25px; top: 16px; font-size: 27px; }
  .flyer--personal .band .mail { position: absolute; left: 25px; top: 53px; font-size: 19px; }
  .flyer--personal .band .tel { position: absolute; left: 25px; top: 80px; font-size: 23px; }
  .brand-small { position: absolute; right: 22px; top: 92px; font-size: 9px; letter-spacing: 0.5px; }
</style>
</head>
<body>

<section class="flyer flyer--business">
  <div class="backdrop" role="img" aria-label="Close-up photo of a fingertip pressing a glowing phone keypad in blue and violet tones"></div>

  <p class="lead">Never miss a</p>
  <h1 class="headline outlined">Business call</h1>
  <p class="tail">again!</p>

  <p class="panel" style="top:190px;height:74px;">• The complete telephone system solution for small businesses!</p>
  <p class="panel" style="top:285px;height:75px;">• With an impressive range of professional call handling features!</p>
  <p class="panel" style="top:378px;height:143px;">• Linkwave Express allows small businesses to be responsive 24/7 by combining your landline and mobile calls.</p>

  <p class="contact-web">www.velvetinemobile.example</p>
  <p class="contact-line">e: info@velvetinemobile.example <span class="tel">t: 0871 463 19 19</span></p>

  <footer class="band">
    <div class="brand-block">
      <span class="brand-mark"></span>
      <span class="brand-name">VELVETINE MOBILE</span>
    </div>
  </footer>
</section>

<section class="flyer flyer--personal">
  <div class="backdrop" role="img" aria-label="Close-up photo of a glowing phone keypad in blue and violet tones"></div>

  <h2 class="question outlined">Never want to miss<br>a call again?</h2>

  <p class="panel" style="top:160px;">• Get your landline number on your mobile.</p>
  <p class="panel" style="top:270px;padding-top:22px;">• Offshore and discrete billing</p>
  <p class="panel" style="top:378px;">• We will save you money of your existing mobile provider.</p>

  <div class="devices" role="img" aria-label="Photo of a Zorphones touchscreen handset beside a Plumleaf keyboard handset"></div>
  <p class="invite outlined">Why not give us a call<br>to see what we can<br>do for you!</p>

  <div class="carriers">
    <span class="dot"></span><span>QX</span><span>K7</span><span>Telmarix</span>
  </div>

  <footer class="band">
    <p class="web">www.velvetinemobile.example</p>
    <p class="mail">e: info@velvetinemobile.example</p>
    <p class="tel">t: 0871 463 19 19</p>
    <p class="brand-small">VELVETINE MOBILE</p>
  </footer>
</section>

</body>
</html>
```